Flyer Design in Photoshop PSD format needed

Christmas Production Flyer - DL (Horizontal) 210 wide x 100 deep

Final file to have elements as layered .psd

We need a flyer design to promote our upcoming Christmas Production which will be based on a movie premier.

Target Market(s)

Young Families Young Adult

Industry/Entity Type

Movie

Requirements
Must have
• The design should look like a Movie poster or Movie Premier advertisement.
Movie Title: Lantern (Main line, focal point) of Tidings (Tag line, possibly italicised)
Dates: 16th and 18th of December
Time: 7pm
Tickets: Booking Online
Price: Free
Address: The Marlowe 412 Wattle St Newcastle
Presented by - Fellowship72

In the strip at the bottom
Parking available at Corvel and Rest Harbour
Starring: Baby Jesus, Mary, Joseph, Gabriel, Choir of Angels

(Colours - midnight style theme/night sky/stars - not heaps of colour - dramatic)
Nice to have
• Theme:
Like as on movie posters e.g. starring. Valmont Screen Gala premier glitz and glam. Monaco.
Star sitting above middle (left to right) shining down onto a manger
Black strip at the bottom like in a movie poster containing most of the info regarding the event.
Should not have
• Snow
Christmas Tree, bobbles and presents, tinsel not kitch

```html
<!DOCTYPE html>
<html lang="en">
<head>
<meta charset="utf-8">
<title>Lantern of Tidings – Christmas Production Flyer</title>
<link rel="stylesheet" href="https://fonts.googleapis.com/css2?family=Cinzel:wght@400;600;700&family=Oswald:wght@400;500;600&display=swap">
<style>
  :root {
    --ink-black: #000000;
    --night-deep: #060b1c;
    --night-mid: #13214a;
    --night-glow: #3a5596;
    --star-white: #ffffff;
    --title-white: #f6f6f4;
    --credit-white: #ffffff;
  }
  * { margin: 0; padding: 0; box-sizing: border-box; }
  html, body {
    width: 1200px; height: 2520px; overflow: hidden;
    background: var(--ink-black);
  }
  .flyer {
    position: relative; width: 1200px; height: 2520px; overflow: hidden;
    background: var(--night-deep);
  }
  .night-sky {
    position: absolute; left: 0; top: 195px; width: 1200px; height: 2325px;
    background:
      radial-gradient(ellipse 160px 200px at 620px 300px, rgba(255,255,255,0.95), rgba(200,220,255,0.35) 45%, rgba(120,150,220,0) 100%),
      radial-gradient(ellipse 700px 900px at 600px 400px, rgba(70,100,170,0.6), rgba(30,50,110,0) 70%),
      linear-gradient(180deg, var(--night-mid) 0%, #101c40 45%, #0c1634 75%, #060b1c 100%);
  }
  .presenter-band {
    position: absolute; left: 0; top: 0; width: 1200px; height: 195px;
    background: var(--ink-black);
    text-align: center; color: var(--star-white);
    font-family: "Oswald", sans-serif;
  }
  .presenter-name {
    position: absolute; left: 0; right: 0; top: 52px;
    font-size: 62px; font-weight: 600; line-height: 1; letter-spacing: 1px;
    text-transform: uppercase;
  }
  .presenter-verb {
    position: absolute; left: 0; right: 0; top: 160px;
    font-size: 28px; font-weight: 500; line-height: 1; letter-spacing: 1px;
  }
  .title {
    position: absolute; left: 0; width: 1200px; text-align: center;
    font-family: "Cinzel", serif; color: var(--title-white);
    text-shadow: 0 4px 14px rgba(0,0,0,0.55);
    line-height: 1;
  }
  .title-main { top: 600px; font-size: 262px; font-weight: 600; }
  .title-link { top: 880px; font-size: 150px; font-weight: 600; }
  .title-tag  { top: 1005px; font-size: 240px; font-weight: 600; }
  .accolade {
    position: absolute; left: 0; width: 1200px; text-align: center;
    font-family: "Cinzel", serif; color: var(--title-white);
  }
  .accolade-opening { top: 1300px; height: 285px; }
  .accolade-selection { top: 1660px; height: 245px; }
  .wreath-half {
    position: absolute; top: 0; width: 120px; height: 100%;
    border: 10px solid rgba(255,255,255,0.85);
    border-radius: 50%;
  }
  .wreath-left { left: 300px; border-right-color: transparent; border-top-color: transparent; }
  .wreath-right { left: 785px; border-left-color: transparent; border-top-color: transparent; }
  .accolade-line { display: block; line-height: 1; }
  .accolade-small { font-size: 38px; font-weight: 400; }
  .accolade-large { font-size: 64px; font-weight: 400; }
  .accolade-opening .l1 { margin-top: 48px; }
  .accolade-opening .l2 { margin-top: 14px; }
  .accolade-opening .l3 { margin-top: 8px; }
  .accolade-opening .l4 { margin-top: 14px; }
  .accolade-selection .l1 { margin-top: 44px; }
  .accolade-selection .l2 { margin-top: 22px; }
  .accolade-selection .l3 { margin-top: 12px; }
  .billing {
    position: absolute; left: 0; width: 1200px; top: 2030px;
    text-align: center; color: var(--credit-white);
    font-family: "Oswald", sans-serif; text-transform: uppercase;
  }
  .billing-row { display: block; line-height: 1; white-space: nowrap; }
  .billing-row + .billing-row { margin-top: 22px; }
  .credit { font-size: 52px; font-weight: 400; letter-spacing: -0.5px; margin-right: 14px; }
  .credit:last-child { margin-right: 0; }
  .label {
    display: inline-block; font-size: 17px; line-height: 1.05; font-weight: 400;
    vertical-align: top; margin-right: 6px; text-align: right;
  }
  .billing-dates { font-size: 64px; font-weight: 600; letter-spacing: 0.5px; }
  .billing-row.billing-dates { margin-top: 18px; }
</style>
</head>
<body>
<main class="flyer">
  <div class="night-sky" role="img" aria-label="Night sky with a bright shining star above a glowing town"></div>

  <header class="presenter-band">
    <div class="presenter-name">Fellowship72</div>
    <div class="presenter-verb">PRESENTS</div>
  </header>

  <h1>
    <span class="title title-main">Lantern</span>
    <span class="title title-link">of</span>
    <span class="title title-tag">Tidings</span>
  </h1>

  <section class="accolade accolade-opening">
    <span class="wreath-half wreath-left" role="img" aria-label="Laurel branch"></span>
    <span class="wreath-half wreath-right" role="img" aria-label="Laurel branch"></span>
    <span class="accolade-line accolade-small l1">Opening Night</span>
    <span class="accolade-line accolade-large l2">CHRISTMAS</span>
    <span class="accolade-line accolade-large l3">2011</span>
    <span class="accolade-line accolade-small l4">International</span>
  </section>

  <section class="accolade accolade-selection">
    <span class="wreath-half wreath-left" role="img" aria-label="Laurel branch"></span>
    <span class="wreath-half wreath-right" role="img" aria-label="Laurel branch"></span>
    <span class="accolade-line accolade-small l1">Official Selection</span>
    <span class="accolade-line accolade-large l2">CHRISTMAS</span>
    <span class="accolade-line accolade-large l3">2011</span>
  </section>

  <footer class="billing">
    <div class="billing-row">
      <span class="label">Starring</span><span class="credit">Baby Jesus</span><span class="credit">Mary</span><span class="credit">Joseph</span><span class="credit">Gabriel</span><span class="credit">Choir of Angels</span>
    </div>
    <div class="billing-row">
      <span class="label">Time</span><span class="credit">7pm</span><span class="label">Tickets</span><span class="credit">Booking Online</span><span class="label">Price</span><span class="credit">Free</span><span class="label">Presented<br>by</span><span class="credit">Fellowship72</span>
    </div>
    <div class="billing-row">
      <span class="label">Address</span><span class="credit">The Marlowe 412 Wattle St New Castle</span>
    </div>
    <div class="billing-row billing-dates">December 16 and 18</div>
    <div class="billing-row">
      <span class="label">Parking</span><span class="credit">Available at Corvel and Rest Harbour</span>
    </div>
  </footer>
</main>
</body>
</html>
```